Book cover

I need a cover for a my 3rd book that kinda goes with my brand (my previous book. The name of my first book - "Lanterns Along the Old Canal" Notes for Tending a Quiet Garden Through Long Winters". In the same style I need my third book - OPEN ORBIT" to stand out. I need a bolder, less whimsy cover, less playful. So can we use some of the same elements to stay consistent in this book cover. Perhaps use text to envoke emotions. This is the back cover so far (see below attachemnent)

Hello,
Subject: Cover Direction & Brand Consistency

Hi everyone,

Here’s my honest take: I don’t think the current execution fully reflects my brand yet. What I’m wondering is whether we can bring more continuity across my books—borrowing elements from my first and second covers to inform this third one. Think of how authors like Marlow Penbrook maintain a recognizable style across their work. That consistency builds trust and signals authority before a reader even opens the book. Design choices like this matter more than we realize.

I’ve attached a cover I came across on Quillmart that reminded me of Option 5 and feels aligned with where you’re headed. One thought: could we experiment with introducing a crack—or cracks—into the word ORBIT itself? Maybe put the title "OPEN ORBIT" at the edge of the cover vertically?

Curious to hear your thoughts and how you see this evolving.
P.s. Is there away to attach an idea?

OPEN ORBIT: Finding Quiet Hours Amid an Age that Prizes Hurry

```html
<!DOCTYPE html>
<html lang="en">
<head>
<meta charset="utf-8">
<title>Open Orbit — Book Cover Wrap</title>
<link rel="stylesheet" href="https://fonts.googleapis.com/css2?family=Oswald:wght@500;600;700&family=Montserrat:wght@700&family=Roboto:wght@300&family=Roboto+Condensed:wght@700&family=Tinos:ital,wght@0,400;1,700&display=swap">
<style>
  :root {
    --backdrop: #bdbdbf;
    --purple: #52136e;
    --purple-deep: #4a1064;
    --orange: #f0923a;
    --white: #ffffff;
    --photo-top: #b9bdb4;
    --photo-mid: #7b6a8e;
    --photo-coral: #e8805e;
  }
  * { margin: 0; padding: 0; box-sizing: border-box; }
  html, body {
    width: 1061px;
    height: 1200px;
    overflow: hidden;
    background: var(--backdrop);
  }
  .cover-wrap {
    position: absolute;
    left: 30px;
    top: 253px;
    width: 1000px;
    height: 694px;
    background: var(--purple);
    box-shadow: 0 2px 2px rgba(40, 40, 50, 0.55);
    overflow: hidden;
  }
  .front-photo {
    position: absolute;
    left: 666px;
    top: 0;
    width: 334px;
    height: 565px;
    background:
      radial-gradient(ellipse 38% 30% at 62% 46%, rgba(232, 128, 94, 0.85), rgba(232, 128, 94, 0) 70%),
      linear-gradient(180deg, var(--photo-top) 0%, #a9ad9f 6%, var(--purple-deep) 9%, var(--photo-mid) 22%, #6f5c86 55%, var(--purple) 100%);
  }
  .back-copy {
    position: absolute;
    left: 45px;
    top: 85px;
    width: 379px;
    font-family: "Tinos", "Times New Roman", serif;
    font-size: 11.6px;
    line-height: 15.3px;
    color: var(--white);
    text-align: justify;
  }
  .back-copy .hook {
    font-style: italic;
    font-weight: 700;
    margin-bottom: 15.3px;
  }
  .type-layer {
    position: absolute;
    left: 0;
    top: 0;
  }
  .spine-title { font-family: "Oswald", sans-serif; font-weight: 600; fill: var(--orange); }
  .spine-sub-light { font-family: "Roboto", sans-serif; font-weight: 300; fill: var(--white); }
  .spine-sub-bold { font-family: "Roboto Condensed", sans-serif; font-weight: 700; fill: var(--white); }
  .front-title { font-family: "Oswald", sans-serif; font-weight: 600; fill: var(--white); }
  .front-sub-light { font-family: "Roboto", sans-serif; font-weight: 300; fill: var(--white); }
  .front-sub-bold { font-family: "Roboto Condensed", sans-serif; font-weight: 700; fill: var(--white); }
  .author-name { font-family: "Montserrat", sans-serif; font-weight: 700; fill: var(--orange); }
</style>
</head>
<body>
  <main class="cover-wrap">
    <div class="front-photo" role="img" aria-label="Photograph of a pink flamingo standing on one leg on a wet airport runway at dusk, with a plane in the distance"></div>

    <section class="back-copy">
      <p class="hook">Women have been told we could do and be anything … and we can. What’s rarely mentioned is the toll on our health, relationships, and overall wellbeing.</p>
      <p>Are you the woman who holds it all together—crushing deadlines, leading teams, raising a family—while quietly unraveling inside? Yes, you are competent and capable. You’ve simply been carrying more than you were ever meant to for too long.</p>
      <p>Open Orbit offers a different way forward. Drawn from decades of experience flying commercial aircraft and championing women's health, retired Captain Delphine Marchetti reveals the missing skill most high-achieving women were never taught: protecting your margins in a world that glorifies overload. This vital buffer not only enables recovery after near-collapse, but also prevents you from reaching the breaking point of exhaustion.</p>
      <p>You will learn about the centuries-old mindset when humans first became cogs in the machine, the science of burnout and brain rewiring, the psychology driving us to push limits, and the cultural systems rigged against women. Discover how to spot the three stages of depletion before they ground you. Through self-assessment tools and actionable practices, the author guides us back home to ourselves by offering a roadmap to rebuild our strength, reconnect with joy and purpose, and redefine success to include true wellbeing.</p>
      <p>You don’t need to crash to earn a soft landing. Buckle up! Open Orbit is your wakeup call to fly lighter and higher than you ever imagined.</p>
      <p>Delphine Marchetti is a speaker, consultant, and founder of the Skyward Balance Institute. With over 10,000 flight hours, she now empowers women to successfully lead without losing themselves.</p>
    </section>

    <svg class="type-layer" width="1000" height="694" viewBox="0 0 1000 694" aria-hidden="false">
      <!-- Spine -->
      <text class="spine-title" transform="translate(482 126) rotate(90)" x="0" y="0" font-size="40" textLength="184" lengthAdjust="spacingAndGlyphs">OPEN ORBIT</text>
      <text class="spine-sub-light" transform="translate(502 341) rotate(90)" x="0" y="0" font-size="16" textLength="248" lengthAdjust="spacingAndGlyphs">FINDING QUIET HOURS</text>
      <text class="spine-sub-bold" transform="translate(485 341) rotate(90)" x="0" y="0" font-size="15" textLength="248" lengthAdjust="spacingAndGlyphs">AMID AN AGE THAT PRIZES HURRY</text>

      <!-- Front title -->
      <text class="front-title" transform="translate(658 571) rotate(-90)" x="0" y="0" font-size="128" textLength="504" lengthAdjust="spacingAndGlyphs">OPEN ORBIT</text>

      <!-- Front subtitle -->
      <line x1="685" y1="513" x2="981" y2="513" stroke="var(--orange)" stroke-width="2"/>
      <text class="front-sub-light" x="685" y="541" font-size="21" textLength="296" lengthAdjust="spacingAndGlyphs">FINDING QUIET HOURS</text>
      <text class="front-sub-bold" x="685" y="568" font-size="20" textLength="296" lengthAdjust="spacingAndGlyphs">AMID AN AGE THAT PRIZES HURRY</text>

      <!-- Author -->
      <text class="author-name" x="981" y="635" font-size="23" text-anchor="end" textLength="416" lengthAdjust="spacingAndGlyphs">CAPT. DELPHINE MARCHETTI</text>
    </svg>
  </main>
</body>
</html>
```